Silver Lantern Golf Club is a golf community dedicated to building productive relationships beginning with the unifying foundation of the great game.
Membership in the Silver Lantern Golf Club is simple, ask to join. The Membership Committee accepts a prospective member request upon confirmation of support for the club’s purpose.
The Silver Lantern Golf Club has only two rules:
1.) Create productive relationships building around an initial common thread
2.) When tempted to cut the last relationship thread, remember rule #1
Silver Lantern Golf Club members receive invitations to occasional club events but are also encouraged to create smaller events hosted by individual members. Members are not required to brand gatherings as official Silver Lantern Golf Club events. We believe when two or more of our members are together, the world gets better.
What are the dues? Members pay dues by sharing great stories, laughing often, encouraging each other to live well and by contributing to a meaningful cause outside of golf. If interested, please make a request for membership on the clubs Flockbook page or send an email request to our Caddie Master at caddiemaster@brovenmail.com.
If you join through our Flockbook page, we encourage you to tag our page with testimonies about your common thread inspired experiences. For example, pictures of golf buddy trips and meaningful moments enjoying the great game with your family and friends.
We focus on what brings people together…
Target Market(s)
golfers who get the need to give back
Colors
Designer to choose colors to be used in the design.
Requirements
Must have
- clear messaging about the simple purpose vof the virtual club
- we can make up head quarter locations. like 19th holes around the world, global fairways, etc
- we do need a link to the club caddiemaster@brovenmail.com
- logo very visible
Nice to have
- course pictures.... I can upload or send a few good ones
Should not have
- Pictures of virtual golf. I changed the summary

```html
<!DOCTYPE html>
<html lang="en">
<head>
<meta charset="utf-8">
<title>Silver Lantern Golf Club – Cover</title>
<link href="https://fonts.googleapis.com/css2?family=Libre+Baskerville:wght@400;700&family=Roboto+Condensed:wght@700&family=Arimo:wght@400;500&display=swap" rel="stylesheet">
<style>
  :root {
    --page: #ffffff;
    --ink: #000000;
    --paper: #ffffff;
    --green: #4cb847;
    --green-text: #7fd13b;
    --sky-top: #2f7fc4;
    --sea: #3a78a8;
    --cliff: #8a7a62;
    --grass: #3f5a24;
  }
  * { margin: 0; padding: 0; box-sizing: border-box; }
  html, body { width: 1200px; height: 1200px; overflow: hidden; background: var(--page); }
  .cover {
    position: absolute; left: 0; top: 378px;
    width: 1200px; height: 444px;
    background: var(--ink); overflow: hidden;
    box-shadow: 0 2px 6px rgba(0,0,0,.35);
  }
  .cover-art { position: absolute; inset: 0; }
  .club-mark {
    position: absolute; left: 40px; top: 66px;
    display: flex; align-items: center; gap: 12px;
    color: var(--paper);
    font-family: "Libre Baskerville", serif; font-weight: 700; font-size: 21px;
  }
  .club-mark .dot {
    width: 34px; height: 34px; border-radius: 50%;
    border: 3px solid var(--paper); flex: none;
  }
  .join-note {
    position: absolute; left: 0; width: 416px; top: 300px;
    text-align: center; color: var(--green-text);
    font-family: "Roboto Condensed", sans-serif; font-weight: 700;
    font-size: 20px; line-height: 25px;
    text-shadow: 0 1px 3px rgba(0,0,0,.6);
  }
  .join-email {
    position: absolute; left: 0; width: 416px; top: 395px;
    text-align: center; color: var(--paper);
    font-family: "Arimo", sans-serif; font-weight: 500;
    font-size: 23px; letter-spacing: 1.2px;
    text-shadow: 0 1px 3px rgba(0,0,0,.6);
  }
  .message {
    position: absolute; left: 535px; width: 600px; top: 26px;
    text-align: center; color: var(--paper);
  }
  .headline { font-family: "Libre Baskerville", serif; font-weight: 400; line-height: 1; }
  .headline .lead { display: block; font-size: 27px; }
  .headline .main { display: block; font-size: 37px; margin-top: 6px; }
  .purpose {
    font-family: "Libre Baskerville", serif; font-size: 17.5px;
    line-height: 31px; margin-top: 12px; letter-spacing: -0.3px;
  }
  .rules-title {
    margin: 14px auto 0; width: 595px; height: 33px; border-radius: 17px;
    background: var(--green);
    font-family: "Roboto Condensed", sans-serif; font-weight: 700;
    font-size: 22px; line-height: 33px;
  }
  .rules { list-style: none; margin-top: 18px; font-family: "Arimo", sans-serif; font-size: 20px; line-height: 25px; }
  .rule { display: flex; align-items: center; justify-content: center; gap: 16px; }
  .rule + .rule { margin-top: 16px; }
  .rule .num {
    width: 36px; height: 36px; border-radius: 50%; flex: none;
    background: var(--green); border: 2px solid var(--paper);
    font-size: 23px; line-height: 32px;
  }
  .rule .text { text-align: center; }
  .rule-one .text { width: 360px; }
  .rule-two .text { width: 440px; }
</style>
</head>
<body>
  <section class="cover">
    <svg class="cover-art" width="1200" height="444" viewBox="0 0 1200 444">
      <defs>
        <linearGradient id="coastTones" x1="0" y1="0" x2="0" y2="1">
          <stop offset="0" stop-color="var(--sky-top)"/>
          <stop offset="0.38" stop-color="#9cc3df"/>
          <stop offset="0.45" stop-color="var(--sea)"/>
          <stop offset="0.62" stop-color="var(--cliff)"/>
          <stop offset="1" stop-color="var(--grass)"/>
        </linearGradient>
      </defs>
      <rect width="600" height="444" fill="url(#coastTones)" role="img" aria-label="Photo of a clifftop golf course above the sea under a blue sky"/>
      <path d="M399 0 Q582 222 413 444 L1200 444 L1200 0 Z" fill="var(--ink)"/>
      <path d="M399 0 Q582 222 413 444" fill="none" stroke="var(--paper)" stroke-width="8"/>
    </svg>

    <div class="club-mark"><span class="dot"></span><span>Silver Lantern Golf Club</span></div>

    <p class="join-note">for membership on the clubs<br>Flockbook page or send an email request to<br>our Caddie Master at</p>
    <p class="join-email">caddiemaster@brovenmail.com</p>

    <div class="message">
      <h1 class="headline"><span class="lead">WE FOCUS ON WHAT BRINGS</span><span class="main">PEOPLE TOGETHER...</span></h1>
      <p class="purpose">Silver Lantern Golf Club is a virtual golf club community dedicated to building productive relationships beginning with the unifying foundation of the great game.</p>
      <h2 class="rules-title">THE SILVER LANTERN GOLF CLUB HAS ONLY TWO RULES</h2>
      <ol class="rules">
        <li class="rule rule-one"><span class="num">1</span><span class="text">Create productive relationships building around an initial common thread.</span></li>
        <li class="rule rule-two"><span class="num">2</span><span class="text">When tempted to cut the last relationship thread, remember rule #1</span></li>
      </ol>
    </div>
  </section>
</body>
</html>
```